Medical Education and Learning Portal refresh

We at Vantrel Limited have developed a learning platform for medical students. It is based around multiple choice questions, but has social and gaming elements built in to make it fun. It will be used on desktop and mobile devices.

I am looking for a refresh of the 'dated' design into something modern and transferrable between devices.

Note that I have a 'focus group' of Medical Students on 4 February where the Top 3-4 designs will be shown to them for them to pick the winner.

I have also uploaded screenshots of the current site. Essentially I would like to reduce the complexity of design into 2-3 pages (currently unlogged in front/home page, logged in page with options, answer questions page, competition page, revision page/summary pages etc). What I am really after is a good clean colour scheme & structure.

If we get the design colour scheme right then I can pay additionally for coding and maybe some additional structure to pages.
Updates

Target Market(s)

Healthcare/Medical Students

Industry/Entity Type

Healthcare

Number of Pages Required

4 page

Font styles to use
Serif
Sans Serif

Requirements
Must have
• 'Clean' Web 2.0 (or later) feel to it.
• I also expect that the images for the trophies are 'cleaned up (each trophy has a bronze/silver/platinum version as users increase their score. I am looking for these to be clean and simple but fun!
• I also need the final design to be transferrable from a desktop browser to a mobile device. I will need designs for home page/content page/Q&A page.
• I previously had a side panel float over the site but that is dated now and I would like to have a page with each element clearly on it and any information would briefly float over this but not take the focus away from the main function of the page.
• I have included the 'bronze', 'silver', 'gold' trophy icons in the files. These are fine in one sense but ideally the colours will blend well too ...
• The following article summarises my must haves:
• http://plumquarry-notes.example/web-design/layout-trend-field-guide/
Nice to have
• Creative concept for presenting MCQ's to students, with a timer and box of information about the question (level of the question, the percent of student who get it right ... etc).
Should not have
• Too much complexity ... clean with a few colours is what I am after
• Note too that my logo is not changing and the colours should blend with this.

```html
<!DOCTYPE html>
<html lang="en">
<head>
<meta charset="utf-8">
<title>Vantrel – Medical Education and Learning Platform</title>
<link href="https://fonts.googleapis.com/css2?family=Open+Sans:wght@400;600;700&display=swap" rel="stylesheet">
<style>
:root{
  --blue:#1f72ad;
  --blue-dark:#0f4e7c;
  --navy:#0b3c5f;
  --orange:#f39321;
  --ink:#3a4650;
  --muted:#7d8a94;
  --line:#d9dfe4;
  --pale:#eef2f5;
  --white:#ffffff;
  --footer:#f2f4f6;
  --bottom:#123f61;
}
*{box-sizing:border-box;margin:0;padding:0}
html,body{width:774px;height:1200px;overflow:hidden}
body{font-family:"Open Sans",Arial,sans-serif;color:var(--ink);background:var(--white);font-size:9px;line-height:1.45}
ul{list-style:none}
.wrap{width:700px;margin:0 auto;position:relative}

/* header */
.site-header{height:44px;background:var(--white)}
.site-header .wrap{display:flex;align-items:center;height:44px}
.brand{display:flex;flex-direction:column}
.brand-name{font-size:19px;font-weight:700;color:var(--blue);line-height:1}
.brand-tag{font-size:6px;color:var(--muted);margin-top:2px}
.search{margin-left:140px;width:190px;height:16px;border:1px solid var(--line);border-radius:2px;font-size:7px;color:#aab3ba;padding:2px 6px}
.auth{display:flex;gap:4px;margin-left:10px}
.btn-small{height:15px;padding:0 9px;font-size:7px;font-weight:600;color:var(--white);border-radius:2px;display:flex;align-items:center}
.btn-small.login{background:var(--blue)}
.btn-small.join{background:var(--orange)}
.social{display:flex;gap:4px;margin-left:auto}
.social span{width:14px;height:14px;border-radius:50%;background:var(--blue)}

/* nav */
.main-nav{height:32px;background:var(--blue)}
.main-nav ul{display:flex;height:32px}
.main-nav li{flex:1;display:flex;flex-direction:column;align-items:center;justify-content:center;color:var(--white);font-size:7px;font-weight:600;border-right:1px solid rgba(255,255,255,.18)}
.main-nav li.active{background:var(--orange)}
.main-nav svg{width:11px;height:11px;margin-bottom:2px}

/* hero */
.hero{height:254px;background:linear-gradient(180deg,#f5f7f9,#e4e9ee)}
.hero .wrap{height:254px;display:flex;align-items:center}
.hero-copy{width:300px}
.hero-title{font-size:17px;font-weight:700;color:var(--blue);line-height:1.2}
.hero-list{margin:12px 0 14px}
.hero-list li{display:flex;align-items:center;gap:6px;font-size:9px;margin-bottom:5px;color:var(--ink)}
.hero-list svg{width:10px;height:10px;flex:none}
.btn{display:inline-block;background:var(--blue);color:var(--white);font-size:8px;font-weight:600;padding:6px 14px;border-radius:2px}
.hero-photo{position:absolute;right:0;top:14px;width:360px;height:240px;background:linear-gradient(135deg,#dfe5ea,#b7c4cf 55%,#8fa2b3)}

/* how it works */
.how{height:270px;background:linear-gradient(180deg,var(--blue-dark),var(--navy));text-align:center;color:var(--white);padding-top:20px}
.how h2{font-size:16px;font-weight:700}
.how p{font-size:8px;opacity:.8;margin-top:2px}
.how-stage{position:relative;width:520px;height:180px;margin:16px auto 0}
.how-video{position:absolute;left:70px;top:0;width:300px;height:180px;background:linear-gradient(135deg,#c9d3db,#7c8e9c);display:flex;align-items:center;justify-content:center}
.how-video svg{width:36px;height:36px}
.how-device{position:absolute;background:#dfe6ec;border:3px solid #f4f6f8;border-radius:4px}
.how-device.tablet{left:360px;top:40px;width:110px;height:130px}
.how-device.phone{left:462px;top:70px;width:48px;height:90px}

/* about */
.about{height:245px;padding-top:26px}
.about .wrap{display:flex;justify-content:space-between}
.about-copy{width:360px}
.about-copy h2{font-size:18px;font-weight:700;color:var(--blue);line-height:1.1}
.about-copy .sub{font-size:8px;color:var(--orange);margin:2px 0 12px}
.about-copy p{font-size:7px;color:var(--muted);margin-bottom:8px}
.read-more{font-size:7px;font-weight:600;color:var(--blue);display:flex;align-items:center;gap:4px}
.feed{width:250px;border:1px solid var(--line);border-radius:2px;background:var(--white)}
.feed-head{display:flex;justify-content:space-between;align-items:center;padding:6px 8px;border-bottom:1px solid var(--line)}
.feed-head strong{font-size:9px}
.feed-follow{font-size:6px;border:1px solid var(--line);border-radius:2px;padding:1px 5px;color:var(--muted)}
.feed-item{display:flex;gap:6px;padding:7px 8px;border-bottom:1px solid var(--pale)}
.feed-item .avatar{width:16px;height:16px;background:var(--blue);flex:none}
.feed-item p{font-size:6px;color:var(--muted);line-height:1.4}
.feed-item b{color:var(--ink);font-weight:600}
.feed-item a{color:var(--blue)}

/* cta band */
.cta{height:110px;background:var(--blue);color:var(--white)}
.cta .wrap{display:flex;justify-content:space-between;padding-top:18px}
.cta h3{font-size:13px;font-weight:700}
.cta p{font-size:7px;opacity:.85;margin:3px 0 8px}
.signup{display:flex}
.signup .field{width:210px;height:16px;background:var(--white);border-radius:2px 0 0 2px;font-size:7px;color:#a7b1b8;padding:2px 6px}
.signup .go{height:16px;background:var(--navy);padding:0 10px;font-size:7px;font-weight:600;display:flex;align-items:center;border-radius:0 2px 2px 0}
.privacy{font-size:7px;margin-top:6px;display:flex;align-items:center;gap:4px}
.ask{width:260px}
.ask h3{display:flex;align-items:center;gap:6px}
.ask svg{width:16px;height:16px}
.btn-orange{display:inline-block;background:var(--orange);font-size:7px;font-weight:600;padding:4px 12px;border-radius:2px}

/* footer */
.site-footer{height:210px;background:var(--footer);padding-top:20px}
.site-footer .wrap{display:flex}
.foot-col{width:210px}
.foot-col.wide{margin-left:auto;width:200px}
.foot-col h4{font-size:8px;font-weight:700;color:var(--blue);letter-spacing:.4px;margin-bottom:6px}
.foot-col li{font-size:7px;color:var(--muted);line-height:1.75}
.foot-col li.current{color:var(--orange)}
.contact dt{font-size:7px;font-weight:600;color:var(--ink);margin-top:4px}
.contact dd{font-size:7px;color:var(--muted)}
.foot-social{display:flex;gap:5px;margin-top:10px}
.foot-social span{width:15px;height:15px;border-radius:50%;background:#9aa7b1}

/* bottom */
.bottom-bar{height:35px;background:var(--bottom);color:rgba(255,255,255,.75)}
.bottom-bar .wrap{display:flex;justify-content:space-between;align-items:center;height:35px;font-size:7px}
.to-top{display:flex;align-items:center;gap:4px}
</style>
</head>
<body>

<header class="site-header">
  <div class="wrap">
    <div class="brand">
      <span class="brand-name">Vantrel</span>
      <span class="brand-tag">The Medical Revision Platform</span>
    </div>
    <div class="search">Search questions…</div>
    <div class="auth">
      <span class="btn-small login">Login</span>
      <span class="btn-small join">Free Sign Up</span>
    </div>
    <div class="social"><span></span><span></span><span></span></div>
  </div>
</header>

<nav class="main-nav">
  <ul class="wrap">
    <li class="active"><svg viewBox="0 0 12 12" fill="#fff"><path d="M6 1 1 5.5h1.5V11h3V8h1v3h3V5.5H11z"/></svg>Home</li>
    <li><svg viewBox="0 0 12 12" fill="#fff"><path d="M2 2h8v6H7l-3 2V8H2z"/></svg>How We Work</li>
    <li><svg viewBox="0 0 12 12" fill="#fff"><circle cx="4" cy="4" r="2"/><circle cx="8.5" cy="4.5" r="1.6"/><path d="M0.5 10.5c0-2.5 1.6-4 3.5-4s3.5 1.5 3.5 4zM8 10.5c0-1.6-.4-2.7-1-3.4 1.9-.6 4.3.6 4.3 3.4z"/></svg>What Your Peers Say</li>
    <li><svg viewBox="0 0 12 12" fill="#fff"><rect x="1.5" y="1.5" width="9" height="9" rx="1"/></svg>Subscription Plan</li>
    <li><svg viewBox="0 0 12 12" fill="#fff"><path d="M1 3h10v6H1z M1 3l5 3.5L11 3" stroke="#1f72ad" stroke-width=".8"/></svg>Contact Us</li>
  </ul>
</nav>

<section class="hero">
  <div class="wrap">
    <div class="hero-copy">
      <h1 class="hero-title">Vantrel - Medical Education and Learning Platform</h1>
      <ul class="hero-list">
        <li><svg viewBox="0 0 10 10"><circle cx="5" cy="5" r="5" fill="#f39321"/><path d="M2.8 5.2 4.4 6.7 7.3 3.5" stroke="#fff" stroke-width="1.2" fill="none"/></svg>Share your registered friends progress.</li>
        <li><svg viewBox="0 0 10 10"><circle cx="5" cy="5" r="5" fill="#f39321"/><path d="M2.8 5.2 4.4 6.7 7.3 3.5" stroke="#fff" stroke-width="1.2" fill="none"/></svg>Earn trophies with increased knowledge</li>
        <li><svg viewBox="0 0 10 10"><circle cx="5" cy="5" r="5" fill="#f39321"/><path d="M2.8 5.2 4.4 6.7 7.3 3.5" stroke="#fff" stroke-width="1.2" fill="none"/></svg>28,000 Questions answered</li>
      </ul>
      <span class="btn">Get Started Now</span>
    </div>
    <div class="hero-photo" role="img" aria-label="Photo of smiling medical professionals in white coats"></div>
  </div>
</section>

<section class="how">
  <h2>How it Work?</h2>
  <p>Take a Tour on our Platform now with Video</p>
  <div class="how-stage">
    <div class="how-video" role="img" aria-label="Video still of hands typing on a laptop keyboard">
      <svg viewBox="0 0 36 36"><circle cx="18" cy="18" r="17" fill="rgba(255,255,255,.85)"/><path d="M14 11v14l11-7z" fill="#0f4e7c"/></svg>
    </div>
    <div class="how-device tablet" role="img" aria-label="Tablet showing the platform"></div>
    <div class="how-device phone" role="img" aria-label="Phone showing the platform"></div>
  </div>
</section>

<section class="about">
  <div class="wrap">
    <div class="about-copy">
      <h2>Vantrel</h2>
      <div class="sub">Medical Education and Learning Platform</div>
      <p>Vantrel brings medical students a clean and focused way to revise. Every topic is built around multiple choice questions written by doctors, checked by tutors and grouped by exam level, so you always know exactly what to study next and how far you have come.</p>
      <p>Track your scores over time, compare progress with friends on your course and earn bronze, silver and platinum trophies as your knowledge grows. Short timed rounds make revision fit between lectures, ward rounds and travel on any device.</p>
      <p>Join thousands of students who answer questions daily and see the results.</p>
      <span class="read-more"><svg width="6" height="6" viewBox="0 0 6 6"><path d="M1 0l4 3-4 3z" fill="#1f72ad"/></svg>Read More</span>
    </div>
    <aside class="feed">
      <div class="feed-head"><strong>Posts</strong><span class="feed-follow">Follow</span></div>
      <div class="feed-item"><span class="avatar"></span><p><b>Vantrel</b> @vantrel<br>New cardiology round is live today. Test yourself on <a>vantrel.example</a></p></div>
      <div class="feed-item"><span class="avatar"></span><p><b>Vantrel</b> @vantrel<br>Congratulations to this week's platinum trophy winners, well done all!</p></div>
      <div class="feed-item"><span class="avatar"></span><p><b>Vantrel</b> @vantrel<br>Finals revision tip: ten questions a day adds up fast. <a>#revision</a></p></div>
    </aside>
  </div>
</section>

<section class="cta">
  <div class="wrap">
    <div class="newsletter">
      <h3>Newsletter</h3>
      <p>Sign up to our mailing list to get new question rounds and exam tips.</p>
      <div class="signup"><span class="field">Enter your email</span><span class="go">SIGN UP</span></div>
      <div class="privacy"><svg width="6" height="6" viewBox="0 0 6 6"><path d="M1 0l4 3-4 3z" fill="#fff"/></svg>Privacy Policy</div>
    </div>
    <div class="ask">
      <h3><svg viewBox="0 0 16 16"><circle cx="8" cy="8" r="8" fill="#fff"/><path d="M6 6.2a2 2 0 1 1 2.6 1.9c-.5.2-.6.5-.6 1.1" stroke="#1f72ad" stroke-width="1.4" fill="none"/><circle cx="8" cy="11.8" r=".9" fill="#1f72ad"/></svg>Post Your Question ?</h3>
      <p>Got your own exam question? Share it with fellow students today.</p>
      <span class="btn-orange">Post Now</span>
    </div>
  </div>
</section>

<footer class="site-footer">
  <div class="wrap">
    <div class="foot-col">
      <h4>RESOURCES</h4>
      <ul>
        <li>Take the Tour</li>
        <li class="current">Welcome Pack</li>
        <li>Subscriptions</li>
        <li>Friends</li>
        <li>Competitions</li>
        <li>Statistics</li>
        <li>Trophies</li>
        <li>Annual Questions</li>
        <li>Past Questions</li>
      </ul>
    </div>
    <div class="foot-col">
      <h4>QUICK LINK</h4>
      <ul>
        <li>Home</li>
        <li>About</li>
        <li>Contact Us</li>
        <li>Privacy Policy</li>
        <li>Terms</li>
        <li>F.A.Q.</li>
        <li>Site Map</li>
      </ul>
    </div>
    <div class="foot-col wide">
      <h4>CONNECT WITH US</h4>
      <dl class="contact">
        <dt>Vantrel Limited</dt>
        <dd>14 Harrow Lane, Westbury WB2 7LN</dd>
        <dt>Phone</dt>
        <dd>+44 0123 456 789</dd>
        <dt>Email</dt>
        <dd>hello@vantrel.example</dd>
      </dl>
      <div class="foot-social"><span></span><span></span><span></span><span></span></div>
    </div>
  </div>
</footer>

<div class="bottom-bar">
  <div class="wrap">
    <span>© 2014 Vantrel Limited. All Rights Reserved</span>
    <span class="to-top"><svg width="7" height="7" viewBox="0 0 7 7"><path d="M0 6l3.5-5L7 6z" fill="rgba(255,255,255,.75)"/></svg>Back to Top</span>
  </div>
</div>

</body>
</html>
```